Bill board design For Marlowe’s Construction

Billboard Design Request
Please design the billboard to match the branding, colors, and overall feel of our website: Marlowe's Construction Website
MARLOWE’S CONSTRUCTION
CONCRETE BUILT FOR GENERATIONS
⭐ 5-Star Rated on Zorvix
Please Include:
* All three attached project photos
* Company logo(s)
* Phone Number: 555-214-7630
* Website: MarlowesConstruction.example
* Zorvix logo with 5-star rating graphic
* Chatterly logo
* Pixtoria logo
Service Area:
Elmsworth • Cedar Hollow • Ashbrook • Stone Ridge
Please arrange the photos and layout in whatever way creates the strongest visual impact and readability from the road. The company name, headline, phone number, and website should be highly visible at highway speeds.
The overall appearance should be clean, professional, premium, and consistent with our website branding while highlighting our reputation, craftsmanship, and quality concrete work.
People Driving By
Concrete Construction

```html
<!DOCTYPE html>
<html lang="en">
<head>
<meta charset="utf-8">
<title>Marlowe’s Construction Billboard</title>
<link rel="stylesheet" href="https://fonts.googleapis.com/css2?family=Montserrat:wght@500;600;700;800&family=Source+Sans+3:wght@400;600&display=swap">
<style>
  :root {
    --brand-blue: #1a8fe3;
    --ink-black: #0f0f10;
    --paper-white: #ffffff;
    --rule-grey: #3a3a3c;
    --sub-grey: #8a8a8e;
    --star-gold: #f6b400;
    --backdrop: #b3b3b3;
    --photo-warm: #9a6a48;
    --photo-green: #6f7e4e;
    --photo-light: #d9d5cf;
  }
  html, body {
    margin: 0;
    padding: 0;
    width: 1200px;
    height: 1200px;
    overflow: hidden;
    background: var(--backdrop);
  }
  .billboard {
    position: absolute;
    left: 50px;
    top: 325px;
    width: 1100px;
    height: 550px;
    overflow: hidden;
    box-shadow: 12px 14px 22px rgba(0,0,0,0.35);
    font-family: "Montserrat", sans-serif;
  }
  .billboard-shapes { position: absolute; inset: 0; }
  .brand {
    position: absolute;
    left: 45px;
    top: 40px;
    width: 340px;
    text-align: center;
    color: var(--brand-blue);
    font-weight: 700;
  }
  .brand-mark {
    width: 62px;
    height: 62px;
    margin: 0 auto 14px;
    background: var(--brand-blue);
  }
  .brand-name { font-size: 44px; line-height: 1; letter-spacing: 0.5px; }
  .brand-sub {
    font-size: 17px;
    font-weight: 500;
    letter-spacing: 4px;
    margin-top: 6px;
    color: var(--sub-grey);
  }
  .rating {
    position: absolute;
    left: 45px;
    top: 238px;
    width: 340px;
    text-align: center;
  }
  .rating-name {
    color: var(--paper-white);
    font-weight: 700;
    font-size: 48px;
    line-height: 1;
  }
  .rating-stars { margin-top: 6px; }
  .services {
    position: absolute;
    left: 435px;
    top: 38px;
    color: var(--paper-white);
  }
  .section-title {
    color: var(--brand-blue);
    font-weight: 700;
    font-size: 30px;
    letter-spacing: 1px;
    padding-bottom: 4px;
    border-bottom: 2px solid var(--brand-blue);
    display: inline-block;
  }
  .service-list { list-style: none; margin: 14px 0 0; padding: 0; }
  .service-item {
    display: flex;
    align-items: center;
    gap: 12px;
    font-size: 28px;
    font-weight: 600;
    height: 43px;
  }
  .service-rule {
    width: 38px;
    height: 2px;
    background: var(--brand-blue);
    margin: 26px 0 22px;
  }
  .social-handle {
    font-family: "Source Sans 3", sans-serif;
    font-size: 24px;
  }
  .social-list { display: flex; gap: 16px; margin-top: 10px; }
  .social-item {
    display: flex;
    align-items: center;
    gap: 6px;
    font-family: "Source Sans 3", sans-serif;
    font-size: 17px;
    font-weight: 600;
    color: var(--brand-blue);
  }
  .social-dot {
    width: 24px;
    height: 24px;
    background: var(--brand-blue);
    border-radius: 4px;
  }
  .service-area {
    position: absolute;
    left: 0;
    width: 1100px;
    top: 383px;
    text-align: center;
  }
  .city-list {
    margin-top: 12px;
    font-weight: 700;
    font-size: 27px;
    color: var(--ink-black);
    letter-spacing: 0.5px;
    white-space: nowrap;
  }
  .city-sep { color: var(--brand-blue); padding: 0 6px; }
  .contact-bar {
    position: absolute;
    left: 0;
    bottom: 0;
    width: 1100px;
    height: 58px;
    background: var(--brand-blue);
    color: var(--paper-white);
    font-family: "Source Sans 3", sans-serif;
    font-size: 40px;
    display: flex;
    align-items: center;
  }
  .contact-phone { display: flex; align-items: center; gap: 22px; margin-left: 50px; }
  .contact-web { display: flex; align-items: center; gap: 22px; margin-left: 70px; }
</style>
</head>
<body>
<main class="billboard">
  <svg class="billboard-shapes" viewBox="0 0 1100 550" width="1100" height="550">
    <rect width="1100" height="550" fill="var(--paper-white)"/>
    <path fill="var(--brand-blue)" d="M0,0 H1100 V350 C900,300 700,318 500,362 C380,390 280,400 200,392 C90,375 20,330 0,258 Z"/>
    <path fill="var(--ink-black)" d="M0,0 H1100 V210 C900,238 700,318 450,372 C330,396 220,394 150,366 C60,322 15,232 0,110 Z"/>
    <line x1="405" y1="45" x2="405" y2="335" stroke="var(--rule-grey)" stroke-width="2"/>
    <defs>
      <linearGradient id="photo-crew" x1="0" y1="0" x2="1" y2="1">
        <stop offset="0" stop-color="var(--photo-green)"/>
        <stop offset="1" stop-color="#3b3f45"/>
      </linearGradient>
      <linearGradient id="photo-drive" x1="0" y1="0" x2="0" y2="1">
        <stop offset="0" stop-color="#6b4a3a"/>
        <stop offset="1" stop-color="var(--photo-warm)"/>
      </linearGradient>
      <linearGradient id="photo-garage" x1="0" y1="0" x2="0" y2="1">
        <stop offset="0" stop-color="#6e6a6c"/>
        <stop offset="1" stop-color="var(--photo-light)"/>
      </linearGradient>
    </defs>
    <circle cx="792" cy="152" r="99" fill="url(#photo-crew)" stroke="var(--brand-blue)" stroke-width="3" role="img" aria-label="Photo: crew finishing fresh concrete in a residential yard"/>
    <circle cx="976" cy="152" r="99" fill="url(#photo-drive)" stroke="var(--brand-blue)" stroke-width="3" role="img" aria-label="Photo: stamped terracotta concrete driveway in front of a home"/>
    <circle cx="882" cy="300" r="97" fill="url(#photo-garage)" stroke="var(--brand-blue)" stroke-width="3" role="img" aria-label="Photo: new smooth concrete driveway leading to a garage"/>
  </svg>

  <div class="brand">
    <div class="brand-mark"></div>
    <div class="brand-name">MARLOWE’S</div>
    <div class="brand-sub">CONSTRUCTION L.L.C</div>
  </div>

  <div class="rating">
    <div class="rating-name">Zorvix</div>
    <svg class="rating-stars" width="140" height="26" viewBox="0 0 140 26" aria-label="5-star rating">
      <g fill="var(--star-gold)">
        <polygon points="13,1 16.5,9 25,9.5 18.5,15 20.5,24 13,19 5.5,24 7.5,15 1,9.5 9.5,9"/>
        <polygon transform="translate(28 0)" points="13,1 16.5,9 25,9.5 18.5,15 20.5,24 13,19 5.5,24 7.5,15 1,9.5 9.5,9"/>
        <polygon transform="translate(56 0)" points="13,1 16.5,9 25,9.5 18.5,15 20.5,24 13,19 5.5,24 7.5,15 1,9.5 9.5,9"/>
        <polygon transform="translate(84 0)" points="13,1 16.5,9 25,9.5 18.5,15 20.5,24 13,19 5.5,24 7.5,15 1,9.5 9.5,9"/>
        <polygon transform="translate(112 0)" points="13,1 16.5,9 25,9.5 18.5,15 20.5,24 13,19 5.5,24 7.5,15 1,9.5 9.5,9"/>
      </g>
    </svg>
  </div>

  <section class="services">
    <div class="section-title">SERVICES</div>
    <ul class="service-list">
      <li class="service-item">
        <svg width="26" height="26" viewBox="0 0 26 26" aria-hidden="true">
          <rect x="2" y="3" width="22" height="20" fill="none" stroke="var(--brand-blue)" stroke-width="2"/>
          <path d="M6 9 H20 M6 13 H20 M6 17 H20" stroke="var(--brand-blue)" stroke-width="2"/>
        </svg>
        CONCRETE
      </li>
      <li class="service-item">
        <svg width="26" height="26" viewBox="0 0 26 26" aria-hidden="true">
          <path d="M2 16 q3 -3 6 0 t6 0 t6 0 t4 0 M2 21 q3 -3 6 0 t6 0 t6 0 t4 0" fill="none" stroke="var(--brand-blue)" stroke-width="2"/>
          <rect x="14" y="4" width="5" height="5" fill="var(--brand-blue)"/>
        </svg>
        POOLS
      </li>
    </ul>
    <div class="service-rule"></div>
    <div class="social-handle">MarlowesConstruction</div>
    <div class="social-list">
      <span class="social-item"><span class="social-dot"></span>Chatterly</span>
      <span class="social-item"><span class="social-dot"></span>Pixtoria</span>
    </div>
  </section>

  <section class="service-area">
    <div class="section-title">SERVICE AREA</div>
    <div class="city-list">
      ELMSWORTH<span class="city-sep">•</span>CEDAR HOLLOW<span class="city-sep">•</span>ASHBROOK<span class="city-sep">•</span>STONE RIDGE
    </div>
  </section>

  <footer class="contact-bar">
    <span class="contact-phone">
      <svg width="34" height="34" viewBox="0 0 24 24" aria-hidden="true">
        <path d="M6.6 10.8c1.4 2.8 3.8 5.2 6.6 6.6l2.2-2.2c.3-.3.7-.4 1-.2 1.1.4 2.3.6 3.6.6.6 0 1 .4 1 1V20c0 .6-.4 1-1 1C10.6 21 3 13.4 3 4c0-.6.4-1 1-1h3.5c.6 0 1 .4 1 1 0 1.3.2 2.5.6 3.6.1.3 0 .7-.2 1z" fill="none" stroke="var(--paper-white)" stroke-width="1.8"/>
      </svg>
      555-214-7630
    </span>
    <span class="contact-web">
      <svg width="34" height="26" viewBox="0 0 34 26" aria-hidden="true">
        <rect x="2" y="2" width="30" height="22" fill="none" stroke="var(--paper-white)" stroke-width="3"/>
        <path d="M2 2 L17 15 L32 2" fill="none" stroke="var(--paper-white)" stroke-width="3"/>
      </svg>
      MarlowesConstruction.example
    </span>
  </footer>
</main>
</body>
</html>
```